Halvorn - Refresh the look and feel of an existing website

We currently have an existing website www.halvornworldadvisory.example however it needs a more refreshed 'look and feel'. We are a professional consultancy that works with large corporate organisations and government. Our 'tag line' is A New Way of Thinking. We want the site to communicate "Innovation" and Leading Edge Thinking.

Target Market(s)

Corporate and Professional Clients - Organisation and Business Change

Industry/Entity Type

Management Consulting

Number of Pages Required

1 page

Font styles to use
Sans Serif

Requirements
Must have
• Must have a professional Corporate look and feel. Header 'imagery' is ok but boxes on front page need changing ... along with the words. The focus on home page needs to 'call out' 3 main consulting areas:-
• - Change & Transformation Specialists
• - Innovative Solutions
• - Digital Transformation
• Tag Line for business is ... A New Way of Thinking (Highlighting Halvorn as 'Thought Leaders' in business)
Nice to have
• Less "words' more imagery. Possibly an area for a 'video' or recent articles/blogs on the front page. Needs to have more of an 'interactive' feel. We are open to suggestions.
Should not have
• NA

```html
<!DOCTYPE html>
<html lang="en">
<head>
<meta charset="utf-8">
<title>Halvorn World Advisory</title>
<link rel="stylesheet" href="https://fonts.googleapis.com/css2?family=Open+Sans:wght@400;600;700&display=swap">
<style>
:root{
  --ink:#2b2b2b;
  --muted:#666;
  --faint:#9aa3ad;
  --navy:#1f3a57;
  --navy-band:#274766;
  --navy-field:#355a7e;
  --btn-dark:#24405e;
  --accent:#4fc1cf;
  --cta:#2aa8dc;
  --panel:#f4f4f4;
  --white:#fff;
}
*{box-sizing:border-box;margin:0;padding:0}
html,body{width:1200px;height:2400px;overflow:hidden}
body{font-family:"Open Sans",Arial,sans-serif;color:var(--ink);background:var(--white);position:relative}
.abs{position:absolute}

/* header */
.site-header{position:absolute;left:0;top:0;width:1200px;height:96px;background:var(--white)}
.site-header .logo-panel{position:absolute;left:0;top:0;width:440px;height:96px;background:#f1f2f3;clip-path:polygon(0 0,100% 0,85% 100%,0 100%)}
.brand{position:absolute;left:100px;top:27px;display:flex;align-items:center;gap:14px}
.brand-dot{width:42px;height:42px;border-radius:50%;background:var(--navy)}
.brand-name{font-size:24px;font-weight:700;color:var(--navy);letter-spacing:1px;line-height:1}
.main-nav{position:absolute;right:98px;top:40px;display:flex;gap:35px;font-size:13.5px;font-weight:600;color:#333}
.main-nav .active{color:var(--accent)}

/* hero */
.hero{position:absolute;left:0;top:96px;width:1200px;height:525px;
  background:linear-gradient(100deg,#b8c7d6 0%,#eef1f4 22%,#f7f8f9 42%,#d9e0e7 58%,#eef2f6 74%,#8fa9c8 100%)}
.hero-shade{position:absolute;left:0;bottom:0;width:1200px;height:200px;background:linear-gradient(180deg,rgba(120,130,140,0),rgba(120,130,140,.35))}
.hero-tag{position:absolute;left:100px;top:400px;height:46px;line-height:46px;padding:0 20px 0 25px;background:rgba(40,50,60,.55);color:#fff;font-size:31px;font-weight:400;letter-spacing:.8px}
.hero-arrow{position:absolute;top:225px;width:24px;height:40px}

/* services */
.service{position:absolute;top:690px;width:300px;text-align:center}
.service-img{width:300px;height:222px;border:3px solid #eee;box-shadow:0 8px 8px -4px rgba(0,0,0,.18)}
.service h3{margin-top:18px;font-size:15.5px;font-weight:600;color:#222;line-height:22px}
.service p{margin-top:18px;font-size:11px;line-height:16px;color:#444}
.btn{display:inline-block;height:27px;line-height:27px;padding:0 18px;font-size:12px;font-weight:600;color:#fff;background:var(--btn-dark)}
.btn.light{background:var(--accent)}

/* about */
.about{position:absolute;left:0;top:1141px;width:1200px;height:390px;background:var(--panel)}
.video{position:absolute;left:100px;top:61px;width:463px;height:267px;background:linear-gradient(180deg,#dfe8ea 0%,#a9bcc0 35%,#7a6c63 60%,#4a4340 100%)}
.video-bar{position:absolute;left:0;bottom:0;width:463px;height:52px;background:rgba(20,20,20,.82)}
.video-progress{position:absolute;left:0;bottom:52px;width:463px;height:4px;background:rgba(255,255,255,.25)}
.video-progress span{display:block;width:60%;height:4px;background:rgba(255,255,255,.6)}
.about h2{position:absolute;left:614px;top:56px;font-size:30px;font-weight:400;color:#222}
.about p{position:absolute;left:616px;top:110px;width:480px;font-size:11px;line-height:21.3px;color:#444;hyphens:auto;-webkit-hyphens:auto}
.about .btn{position:absolute;left:614px;top:301px}

/* articles */
.articles h2{position:absolute;left:100px;top:1572px;font-size:29px;font-weight:400;color:#222}
.article{position:absolute;top:1632px;width:322px}
.article-img{width:322px;height:186px}
.article h4{position:absolute;left:59px;top:203px;font-size:13px;font-weight:400;color:#333;white-space:nowrap}
.article .meta{position:absolute;left:59px;top:225px;font-size:9.5px;color:var(--faint);white-space:nowrap}
.article svg.pencil{position:absolute;left:0;top:206px}

/* cta band */
.cta-band{position:absolute;left:0;top:1966px;width:1200px;height:85px;background:var(--navy-band)}
.cta-band p{position:absolute;left:253px;top:28px;font-size:19px;color:#fff;letter-spacing:.6px}
.cta-band .cta-btn{position:absolute;left:760px;top:24px;width:150px;height:37px;line-height:37px;text-align:center;background:var(--cta);color:#fff;font-size:15px;font-weight:600}

/* footer */
.site-footer{position:absolute;left:0;top:2051px;width:1200px;height:349px;background:var(--navy);color:#c3cfdb}
.footer-col{position:absolute;top:32px}
.footer-col h5{font-size:11.5px;font-weight:600;color:#e6ecf2;letter-spacing:.4px;margin-bottom:20px}
.footer-col ul{list-style:none;font-size:11.5px;line-height:30.5px}
.contact-item{display:flex;gap:14px;font-size:11.5px;line-height:19px;padding-bottom:9px;margin-bottom:9px;border-bottom:1px solid #2d4a68}
.contact-item svg{flex:none;margin-top:3px}
.socials{display:flex;gap:17px;margin-top:8px;padding-left:3px}
.socials span{width:13px;height:13px;background:#c3cfdb;border-radius:50%}
.form-field{width:231px;height:29px;background:var(--navy-field);margin-bottom:5px;font-size:10px;color:#fff;padding:7px 8px}
.form-field.tall{height:67px}
.send-btn{margin:18px 0 0 101px;width:130px;height:27px;line-height:27px;text-align:center;background:#1a3049;color:#fff;font-size:10px;font-weight:600}
.copyright{position:absolute;left:0;width:1200px;text-align:center;font-size:11px;color:#c3cfdb}
.copyright span{color:var(--cta)}
</style>
</head>
<body>

<header class="site-header">
  <div class="logo-panel"></div>
  <div class="brand"><span class="brand-dot"></span><span class="brand-name">HALVORN</span></div>
  <nav class="main-nav">
    <span class="active">✻ Home</span><span>About Us</span><span>Our Services</span><span>Solutions</span><span>What's Happening</span><span>Contact Us</span>
  </nav>
</header>

<section class="hero" role="img" aria-label="Photo of a team of business people meeting around a laptop in a bright office">
  <div class="hero-shade"></div>
  <svg class="hero-arrow" style="left:18px" viewBox="0 0 24 40"><path d="M18 4 4 20l14 16" fill="none" stroke="#fff" stroke-opacity=".7" stroke-width="3"/></svg>
  <svg class="hero-arrow" style="right:18px" viewBox="0 0 24 40"><path d="M6 4l14 16L6 36" fill="none" stroke="#fff" stroke-opacity=".7" stroke-width="3"/></svg>
  <div class="hero-tag">A New Way of Thinking</div>
</section>

<section class="services">
  <article class="service" style="left:99px">
    <div class="service-img" role="img" aria-label="Photo of hands working on a laptop at a wooden table" style="background:linear-gradient(180deg,#3f6a2e 0%,#5c8a44 25%,#2f3a26 50%,#8a5a3e 70%,#c99a78 100%)"></div>
    <h3>Change &amp; Transformation Specialists</h3>
    <p>Lorem ipsum dolor sit amet, consectetur adipiscing elit. Aenean commodo nisl ultricies magna malesuada, nec euismod leo auctor. Duis blandit</p>
    <div style="margin-top:24px"><span class="btn light">Read More</span></div>
  </article>
  <article class="service" style="left:450px">
    <div class="service-img" role="img" aria-label="Photo of a person holding a tablet in warm light" style="background:linear-gradient(125deg,#f6e3d0 0%,#d9a07a 30%,#a4542c 55%,#5a2a16 80%,#2e150c 100%)"></div>
    <h3>Innovative Solutions</h3>
    <p>Lorem ipsum dolor sit amet, consectetur adipiscing elit. Aenean commodo nisl</p>
    <div style="margin-top:40px"><span class="btn">Read More</span></div>
  </article>
  <article class="service" style="left:801px">
    <div class="service-img" role="img" aria-label="Photo of a businessman holding a tablet with floating digital app icons" style="background:radial-gradient(circle at 58% 48%,#9ecdf0 0%,#3f7fc4 25%,#253a57 55%,#141c28 100%)"></div>
    <h3>Digital Transformation</h3>
    <p>Lorem ipsum dolor sit amet, consectetur adipiscing elit. Aenean commodo nisl ultricies magna malesuada, nec euismod leo auctor.</p>
    <div style="margin-top:24px"><span class="btn">Read More</span></div>
  </article>
</section>

<section class="about">
  <div class="video" role="img" aria-label="Video still of a smiling team gathered around a table in an office">
    <div class="video-progress"><span></span></div>
    <div class="video-bar">
      <svg width="463" height="52" viewBox="0 0 463 52">
        <g fill="#fff">
          <rect x="54" y="19" width="3" height="14"/><path d="M70 19v14l-12-7z"/>
          <path d="M94 19v14l-9-7zM104 19v14l-9-7z"/>
          <path d="M360 19v14l9-7zM370 19v14l9-7z"/>
          <path d="M392 19v14l12-7z"/><rect x="405" y="19" width="3" height="14"/>
        </g>
        <circle cx="232" cy="26" r="15" fill="none" stroke="#fff" stroke-width="2.5"/>
        <rect x="226" y="19" width="4" height="14" fill="#fff"/><rect x="234" y="19" width="4" height="14" fill="#fff"/>
      </svg>
    </div>
  </div>
  <h2>About Us</h2>
  <p>Integer tristique dui ac sem dapibus aliquet. Praesent ut condimentum urna. Praesent vel suscipit nibh, et vulputate neque. Donec dignissim dui non maximus varius. Aliquam pulvinar dictum quam, vitae imperdiet risus egestas quis. Nam interdum odio vitae sapien feugiat, vitae mattis eros tempus. Cras ornare ex vel turpis posuere porta a nec tellus. Maecenas feugiat placerat tortor nec aliquam. Nulla dolor arcu, tristique nec tempor fermentum, dignissim non urna. Morbi sodales diam quis sollicitudin tristique. Donec sit amet purus hendrerit, aliquam urna vel, lobortis elit.</p>
  <span class="btn">Read More</span>
</section>

<section class="articles">
  <h2>Recent Articles</h2>
  <svg class="abs" style="left:1056px;top:1592px" width="46" height="20" viewBox="0 0 46 20">
    <circle cx="10" cy="10" r="8" fill="none" stroke="#ccc" stroke-width="1.5"/><path d="M12 6l-4 4 4 4" fill="none" stroke="#ccc" stroke-width="1.5"/>
    <circle cx="35" cy="10" r="8" fill="none" stroke="#666" stroke-width="1.5"/><path d="M33 6l4 4-4 4" fill="none" stroke="#666" stroke-width="1.5"/>
  </svg>
  <article class="article" style="left:99px">
    <div class="article-img" role="img" aria-label="Photo of a hand touching a glowing blue network interface" style="background:linear-gradient(135deg,#07183a 0%,#1c4f9c 35%,#6fa8e6 55%,#1b3f7c 75%,#06122a 100%)"></div>
    <svg class="pencil" width="30" height="30" viewBox="0 0 30 30"><path d="M6 24l2-7L20 5l5 5-12 12z M8 17l5 5" fill="none" stroke="#bbb" stroke-width="1.5"/></svg>
    <h4>Post great and long name</h4>
    <div class="meta">14.04.2016 &nbsp; by Admin &nbsp; in Tech, Webnews</div>
  </article>
  <article class="article" style="left:438px">
    <div class="article-img" role="img" aria-label="Photo of hands holding a tablet over a wooden desk" style="background:linear-gradient(135deg,#a56a44 0%,#6b3e24 35%,#2b2b30 55%,#5a3622 75%,#2a1a12 100%)"></div>
    <svg class="pencil" width="30" height="30" viewBox="0 0 30 30"><path d="M6 24l2-7L20 5l5 5-12 12z M8 17l5 5" fill="none" stroke="#bbb" stroke-width="1.5"/></svg>
    <h4>Post great and long name</h4>
    <div class="meta">14.04.2016 &nbsp; by Admin &nbsp; in Tech, Webnews</div>
  </article>
  <article class="article" style="left:779px">
    <div class="article-img" role="img" aria-label="Photo of a hand drawing a chart in bright sunlight" style="background:linear-gradient(150deg,#fbf6ea 0%,#e6dfd0 30%,#9aa0a4 55%,#55606a 80%,#3c434b 100%)"></div>
    <svg class="pencil" width="30" height="30" viewBox="0 0 30 30"><path d="M6 24l2-7L20 5l5 5-12 12z M8 17l5 5" fill="none" stroke="#bbb" stroke-width="1.5"/></svg>
    <h4>Post great and long name</h4>
    <div class="meta">14.04.2016 &nbsp; by Admin &nbsp; in Tech, Webnews</div>
  </article>
</section>

<section class="cta-band">
  <p>Ut auctor sed dolor ut imperdiet. Cras lectus mauris</p>
  <span class="cta-btn">Contact Now</span>
</section>

<footer class="site-footer">
  <div class="footer-col" style="left:99px">
    <h5>ABOUT US</h5>
    <ul><li>Our Team</li><li>Our Values</li><li>Giving Back</li></ul>
  </div>
  <div class="footer-col" style="left:293px">
    <h5>OUR SERVICES</h5>
    <ul><li>Strategy and Design</li><li>Transformation</li><li>Change &amp; Culture</li><li>Organisational Development</li><li>Project Management</li><li>Organisational Efficiency</li></ul>
  </div>
  <div class="footer-col" style="left:548px;width:230px">
    <h5>CONTACT INFO</h5>
    <div class="contact-item"><svg width="14" height="12" viewBox="0 0 14 12"><rect x="1" y="1" width="12" height="10" fill="none" stroke="#c3cfdb" stroke-width="1.4"/><path d="M1 1l6 5 6-5" fill="none" stroke="#c3cfdb" stroke-width="1.4"/></svg><span>info@halvornworldadvisory.example</span></div>
    <div class="contact-item"><svg width="14" height="14" viewBox="0 0 14 14"><path d="M3 1l3 3-2 2c1 2 2 3 4 4l2-2 3 3-2 2C6 13 1 8 1 3z" fill="#c3cfdb"/></svg><span>1300 555 218 (Aus)<br>0800 555 218 (NZ)</span></div>
    <div class="contact-item"><svg width="14" height="16" viewBox="0 0 14 16"><path d="M7 1a5 5 0 0 1 5 5c0 4-5 9-5 9S2 10 2 6a5 5 0 0 1 5-5z" fill="#c3cfdb"/><circle cx="7" cy="6" r="2" fill="#1f3a57"/></svg><span>4410 Harbourline Ave, Ste 12<br>Marlow Bay, FL 33900</span></div>
    <div class="socials"><span></span><span></span><span></span><span></span><span></span><span></span></div>
  </div>
  <div class="footer-col" style="left:870px">
    <h5>CONTACT NOW</h5>
    <div class="form-field">Name</div>
    <div class="form-field">Email Address</div>
    <div class="form-field tall">Message</div>
    <div class="send-btn">SEND</div>
  </div>
  <div class="copyright" style="top:314px">Copyright © 2016 - <span>yoursite</span></div>
</footer>

</body>
</html>
```